Pool Builder Website Design in arizona

Our current site is located here: kelvaro.net

We are looking to give this a modern facelift. We will be cutting your design into a wordpress theme so we can utilize the CMS plateform backend.

Look and Feel
• Clean cut and professional
• Mobile friendly
• Updated from old site
• Feel intrigued but relax (do you have trust logos? Marla looking into this)
Colors
• Warm tropical neutral colors
• Orange, brown, blues
- Please make the site modern and more sleek look that looks like a 2015 style design and NOT 1999.
- Must be coded as a wordpress theme
- must create a home page, inner page and blog page
- must allow client to BLOG using the post section in wordpress

This pool company is a pool builder/installer in Phoenix arizona.

NOTE::: Please create a home page and one internal page.

Serif
Sans Serif

• - Must be coded as a wordpress theme
• - must create a home page, inner page and blog page
• - must allow client to BLOG using the post section in wordpress

```html
<!DOCTYPE html>
<html lang="en">
<head>
<meta charset="utf-8">
<title>Saguaro Pools – The Fiberglass Pool Experts</title>
<link href="https://fonts.googleapis.com/css2?family=Open+Sans:wght@300;400;600;700&display=swap" rel="stylesheet">
<style>
:root{
  --orange:#f07c21;
  --ink:#333b44;
  --muted:#6f7780;
  --link:#3f82d6;
  --sky:#b9d9e6;
  --sky-line:#9fbfcc;
  --card-line:#cfe3ec;
  --deep:#1d3f66;
  --deep-2:#173456;
  --gold:#e7c64a;
  --band:#71879f;
  --footer:#20508f;
  --footer-text:#d9e6f6;
  --bottom:#5d8fd3;
  --brand-blue:#2f6fb8;
  --brand-green:#a8d888;
  --white:#ffffff;
}
*{box-sizing:border-box;margin:0;padding:0}
html,body{width:1200px;height:2472px;overflow:hidden}
body{font-family:"Open Sans",Arial,sans-serif;color:var(--ink);background:var(--white);position:relative;font-size:13px}

/* top bar */
.topbar{position:absolute;top:0;left:0;width:1200px;height:46px;background:var(--white);font-size:12px;color:var(--ink)}
.topbar .phone{position:absolute;left:158px;top:12px;display:flex;align-items:center;gap:14px}
.topbar .phone-icon{width:24px;height:24px;background:var(--orange);display:flex;align-items:center;justify-content:center}
.search{position:absolute;left:386px;top:14px;width:164px;height:20px;border:1px solid #c9ccd0;border-radius:2px;font-size:10px;color:#999;padding:3px 8px}
.search svg{position:absolute;right:6px;top:4px}
.lang{position:absolute;left:616px;top:15px;font-size:10px;display:flex;gap:8px;align-items:center}
.follow{position:absolute;left:839px;top:15px;font-size:10px;display:flex;gap:8px;align-items:center}
.follow .dots{display:flex;gap:3px}
.follow .dots span{width:9px;height:9px;display:block}

/* header */
.brand{position:absolute;left:181px;top:60px;width:165px;height:108px}
.brand .mark{width:24px;height:24px;border-radius:50%;background:#6bbf4e;position:absolute;left:0;top:4px}
.brand .name{position:absolute;left:0;top:34px;font-size:25px;font-weight:700;color:var(--brand-blue);line-height:26px}
.brand .bar{position:absolute;left:0;top:92px;width:160px;height:10px;background:var(--brand-green)}
.nav{position:absolute;left:584px;top:59px;display:flex;gap:3px}
.nav-item{width:87px;text-align:center;font-size:12px;color:var(--ink)}
.nav-thumb{height:86px;margin-bottom:8px}

/* hero */
.hero{position:absolute;top:181px;left:0;width:1200px;height:443px;background:linear-gradient(180deg,#9cc6d6 0%,#dfe6d8 30%,#6f8a4e 48%,#3fb2e0 62%,#24a7dd 75%,#d6c7a8 100%)}

/* welcome section */
.lagoon{position:absolute;top:624px;left:0;width:1200px;height:831px;background:var(--sky)}
.welcome{position:absolute;top:32px;left:124px;width:900px;height:112px}
.welcome .palm{position:absolute;left:172px;top:0;width:110px;height:112px;background:radial-gradient(circle at 50% 40%,#5d9fc8,#7db3d4 70%,transparent 71%)}
.welcome h1{position:absolute;left:237px;top:92px;font-size:21px;font-weight:400;white-space:nowrap;color:#2b3640}
.welcome h1 strong{font-weight:700}
.rule{position:absolute;left:171px;width:858px;height:1px;background:var(--sky-line)}
.features{position:absolute;top:201px;left:171px;display:flex;gap:27px}
.feature{width:266px;height:225px;border:1px solid var(--card-line);position:relative}
.feature .thumb{position:absolute;left:0;top:0;width:118px;height:110px}
.feature h3{position:absolute;left:136px;top:30px;font-size:13px;font-weight:600;color:#2b3640}
.feature .sub{position:absolute;left:136px;top:50px;font-size:10px;color:var(--muted)}
.feature p{position:absolute;left:12px;top:125px;width:246px;font-size:12.5px;line-height:19px;color:var(--muted)}
.more{color:var(--link);font-size:12.5px}
.feature .more{position:absolute;left:12px;top:192px}

.section-title{font-size:16px;font-weight:400;color:#2b3640}
.portfolio-title{position:absolute;left:171px;top:483px}
.tabs{position:absolute;left:171px;top:514px;display:flex;gap:20px;font-size:12px;color:#3a434c}
.tabs .active{color:var(--orange);position:relative}
.tabs .active::after{content:"";position:absolute;left:0;bottom:-7px;width:18px;height:3px;background:var(--orange)}
.arrows{position:absolute;display:flex;gap:2px}
.arrows span{width:17px;height:17px;border:1px solid currentColor;display:flex;align-items:center;justify-content:center}
.arrows.light{left:990px;top:506px;color:#3f6c9a}
.arrows.dark{left:990px;top:8px;color:#e6eef7}
.grid4{position:absolute;left:171px;display:flex;gap:22px}
.work{width:200px;height:251px;border:1px solid var(--card-line)}
.work .thumb{height:162px}
.work h4{font-size:12.5px;font-weight:600;margin:18px 8px 8px;color:#2b3640}
.work p{font-size:12px;line-height:18px;color:var(--muted);margin:0 8px}

/* installation */
.install{position:absolute;top:1455px;left:0;width:1200px;height:380px;background:linear-gradient(135deg,var(--deep) 0%,#23507a 45%,var(--deep-2) 100%)}
.install .section-title{position:absolute;left:171px;top:30px;color:var(--white)}
.step{width:200px;height:291px;border:1px solid #7fa0c0;background:rgba(10,30,55,.35);overflow:hidden}
.step .thumb{height:139px}
.step h4{font-size:12px;font-weight:400;color:var(--gold);margin:14px 10px 0}
.step h4::after{content:"";display:block;width:18px;height:2px;background:var(--orange);margin-top:5px}
.step p{font-size:12px;line-height:20px;color:var(--white);margin:12px 10px 0}

/* testimonial */
.testimonial-title{position:absolute;left:171px;top:1868px}
.avatar{position:absolute;left:171px;top:1910px;width:53px;height:72px;background:linear-gradient(180deg,#b9b2a8,#7d7469)}
.person{position:absolute;left:171px;top:1984px;font-size:12px}
.person .role{font-size:10px;color:var(--muted);display:block;margin-top:2px;letter-spacing:.3px}
.quote-mark{position:absolute;left:257px;top:1934px}
.quote{position:absolute;left:314px;top:1926px;width:715px;font-size:12.5px;line-height:21px;color:var(--muted)}
.pager{position:absolute;left:576px;top:2004px;display:flex;gap:8px}
.pager span{width:10px;height:10px;border-radius:50%;background:#4a5259}
.pager span.on{background:transparent;border:1px solid #4a5259}

/* subscribe */
.subscribe{position:absolute;top:2054px;left:0;width:1200px;height:99px;background:var(--band)}
.subscribe p{position:absolute;top:17px;width:1200px;text-align:center;color:#eef2f7;font-size:15px;font-weight:300}
.subscribe .field{position:absolute;left:295px;top:48px;width:538px;height:28px;background:#5b7290;border:1px solid #8ea1b8;color:#e6ecf3;font-size:12px;padding:5px 10px}
.subscribe .field svg{position:absolute;right:10px;top:8px}
.subscribe .submit{position:absolute;left:833px;top:48px;width:70px;height:28px;background:var(--deep);color:var(--white);font-size:12.5px;font-weight:600;text-align:center;line-height:28px}

/* footer */
.footer{position:absolute;top:2153px;left:0;width:1200px;height:278px;background:var(--footer);color:var(--footer-text);font-size:12.5px;line-height:19px}
.footer h5{font-size:16px;font-weight:400;color:var(--white);position:absolute;top:30px;white-space:nowrap}
.col{position:absolute}
.col.about{left:171px;width:250px}
.col.blog{left:470px;width:270px}
.col.contact{left:763px;width:280px}
.footer-brand{position:absolute;top:72px;left:0;display:flex;align-items:center;gap:8px;font-size:16px;font-weight:700;color:#7fa7d8;white-space:nowrap}
.footer-brand span.dot{width:16px;height:16px;border-radius:50%;background:#7fa7d8}
.about p{position:absolute;top:130px;width:230px}
.about .more{position:absolute;top:197px;color:#8ab6ec}
.post{position:absolute;left:0;display:flex;gap:12px;width:270px}
.post .thumb{width:76px;height:58px;flex:none;margin-top:12px}
.post .meta{font-size:10px;color:#9fbbe0;line-height:14px}
.post .title{color:var(--white);font-size:12.5px}
.post .more{font-size:12px;color:#8ab6ec}
.contact ul{list-style:none;position:absolute;top:66px}
.contact li{display:flex;gap:6px;align-items:flex-start;margin-bottom:9px;color:var(--white)}
.contact li svg{flex:none;margin-top:3px}
.social{position:absolute;top:216px;left:8px;display:flex;gap:18px}
.social span{width:12px;height:12px;border-radius:50%;background:#a9c3e6;display:block}
.social-line{position:absolute;top:236px;left:6px;width:16px;height:2px;background:var(--orange)}

.bottom{position:absolute;top:2431px;left:0;width:1200px;height:41px;background:var(--bottom);color:#0f2a4d;font-size:12px}
.bottom .copy{position:absolute;left:176px;top:11px}
.bottom .top-btn{position:absolute;left:996px;top:6px}

/* photo fills */
.ph-pool{background:linear-gradient(160deg,#cfe4ef,#3aa6dc 55%,#1f7fb8)}
.ph-garden{background:linear-gradient(160deg,#7a8a5c,#3e6a7e 60%,#2e90c2)}
.ph-teal{background:linear-gradient(160deg,#c9b08a,#3fc1c9 55%,#2aa6ad)}
.ph-yard{background:linear-gradient(170deg,#d9d4cc,#b8a48e 60%,#9a8a76)}
.ph-fire{background:linear-gradient(170deg,#f2f0ec,#c6a388 55%,#a27d60)}
.ph-spa{background:linear-gradient(170deg,#b07b5c,#3f9fd6 60%,#2c6fa6)}
.ph-rock{background:linear-gradient(170deg,#a9b8c4,#7a6a58 50%,#3e8fb0)}
.ph-dirt{background:linear-gradient(170deg,#d8c7a6,#b3946b 60%,#8f7350)}
.ph-crane{background:linear-gradient(170deg,#efe9df,#5aa0d4 50%,#c9b89e)}
.ph-deck{background:linear-gradient(180deg,#c9d9e6 0%,#f1f1ee 30%,#a89a88 70%,#8a7c6a)}
.ph-final{background:linear-gradient(180deg,#eae6dc 0%,#6a4e3a 30%,#2c6f86 70%,#bfb3a0)}
.ph-night{background:linear-gradient(160deg,#2a3a55,#3b7fb0 60%,#c99a5a)}
</style>
</head>
<body>

<header>
  <div class="topbar">
    <div class="phone">
      <span class="phone-icon">
        <svg width="14" height="14" viewBox="0 0 14 14"><circle cx="7" cy="4.5" r="3" fill="#fff"/><path d="M1.5 13c0-3 2.5-5 5.5-5s5.5 2 5.5 5z" fill="#fff"/></svg>
      </span>
      <span>555-214-0370</span>
    </div>
    <div class="search">Search...
      <svg width="11" height="11" viewBox="0 0 11 11"><circle cx="6.5" cy="4.5" r="3.3" fill="none" stroke="#777" stroke-width="1.2"/><path d="M4 7 1 10" stroke="#777" stroke-width="1.4"/></svg>
    </div>
    <div class="lang">
      <svg width="14" height="9" viewBox="0 0 14 9"><path d="M0 4.5 4 0v3h6V0l4 4.5L10 9V6H4v3z" fill="#444"/></svg>
      <span>Change your language: English</span>
    </div>
    <div class="follow">
      <span>Follow us:</span>
      <span class="dots"><span style="background:#3b5fa8"></span><span style="background:#3aa3e3"></span><span style="background:#d2452f"></span><span style="background:#cf2b2b"></span></span>
    </div>
  </div>

  <div class="brand">
    <span class="mark"></span>
    <span class="name">Saguaro<br>Pools</span>
    <span class="bar"></span>
  </div>

  <nav class="nav">
    <div class="nav-item"><div class="nav-thumb ph-pool" role="img" aria-label="Photo of a pool style"></div>Style</div>
    <div class="nav-item"><div class="nav-thumb ph-night" role="img" aria-label="Collage of portfolio pool photos"></div>Portfolio</div>
    <div class="nav-item"><div class="nav-thumb ph-yard" role="img" aria-label="Photo of a pool installation"></div>Installation</div>
    <div class="nav-item"><div class="nav-thumb ph-pool" role="img" aria-label="Photo of a family in a pool"></div>About Us</div>
    <div class="nav-item"><div class="nav-thumb ph-teal" role="img" aria-label="Photo of children swimming"></div>Contact Us</div>
  </nav>
</header>

<section class="hero" role="img" aria-label="Photo of a villa with a blue pool, palm trees and wooden sun loungers"></section>

<section class="lagoon">
  <div class="welcome">
    <div class="palm" role="img" aria-label="Palm tree emblem"></div>
    <h1><strong>Welcome to Saguaro pools!</strong> The Fiberglass pool Experts.</h1>
  </div>
  <div class="rule" style="top:162px"></div>

  <div class="features">
    <article class="feature">
      <div class="thumb ph-pool" role="img" aria-label="Photo of a kidney-shaped pool"></div>
      <h3>Pool Sizes</h3>
      <span class="sub">Perfect fit for your needs!</span>
      <p>The dimensions for most of our fiberglass pool and spa shells are below.</p>
      <a class="more">Read More...</a>
    </article>
    <article class="feature">
      <div class="thumb ph-garden" role="img" aria-label="Photo of a pool with wooden fence and garden"></div>
      <h3>Pool Styles</h3>
      <span class="sub">Right pool style for you!</span>
      <p>Saguaro Pools has nearly every brand and style of fiberglass pools to choose from, whether big or small.</p>
      <a class="more">Read More...</a>
    </article>
    <article class="feature">
      <div class="thumb ph-teal" role="img" aria-label="Photo of a turquoise pool with flowers"></div>
      <h3>Pool Colours</h3>
      <span class="sub">Take a look!</span>
      <p>We build fiberglass Pools and Spas in all different colors.</p>
      <a class="more">Read More...</a>
    </article>
  </div>
  <div class="rule" style="top:441px"></div>

  <h2 class="section-title portfolio-title">Portfolio</h2>
  <div class="tabs"><span class="active">All</span><span>Pools</span><span>Spools n Spas</span><span>Firescapes</span><span>Water features</span></div>
  <div class="arrows light">
    <span><svg width="6" height="8" viewBox="0 0 6 8"><path d="M5 0 1 4l4 4" fill="none" stroke="currentColor"/></svg></span>
    <span><svg width="6" height="8" viewBox="0 0 6 8"><path d="m1 0 4 4-4 4" fill="none" stroke="currentColor"/></svg></span>
  </div>
  <div class="grid4" style="top:551px">
    <article class="work"><div class="thumb ph-pool" role="img" aria-label="Photo of a custom fiberglass pool with handrails"></div><h4>Custom Fiberglass Pool</h4><p>Harbor Sapphire Blue with Dual Handrails</p></article>
    <article class="work"><div class="thumb ph-fire" role="img" aria-label="Photo of a beehive fireplace with flagstone seats"></div><h4>Firescape</h4><p>Beehive<br>w/ flagstone seats</p></article>
    <article class="work"><div class="thumb ph-spa" role="img" aria-label="Photo of a spa with spillway into a pool"></div><h4>Spools n Spas</h4><p>Sierra Spa<br>w/ Spillway &amp; Ledgestone Facet</p></article>
    <article class="work"><div class="thumb ph-rock" role="img" aria-label="Photo of a rock waterfall with grotto"></div><h4>Water Features</h4><p>Custom waterfall with grotto jump rock</p></article>
  </div>
</section>

<section class="install">
  <h2 class="section-title">Installation</h2>
  <div class="arrows dark">
    <span><svg width="6" height="8" viewBox="0 0 6 8"><path d="M5 0 1 4l4 4" fill="none" stroke="currentColor"/></svg></span>
    <span><svg width="6" height="8" viewBox="0 0 6 8"><path d="m1 0 4 4-4 4" fill="none" stroke="currentColor"/></svg></span>
  </div>
  <div class="grid4" style="top:70px">
    <article class="step"><div class="thumb ph-dirt" role="img" aria-label="Photo of workers digging the pool hole"></div><h4>Digging and Leveling</h4><p>After we stake the area out, we dig the hole for your pool or spa and they spread the sand base to make it level.</p></article>
    <article class="step"><div class="thumb ph-crane" role="img" aria-label="Photo of a pool shell being lowered by crane"></div><h4>Placing the Pool</h4><p>After the hole is perfectly dug, we lower the pool gently with a crane.Our crew is meticulous about getting it done right.</p></article>
    <article class="step"><div class="thumb ph-deck" role="img" aria-label="Photo of a new pool deck and patio"></div><h4>Installing the Pump</h4><p>Then we install pumps and and a patio around the pool and begin to make your pool "a small bit of paradise".</p></article>
    <article class="step"><div class="thumb ph-final" role="img" aria-label="Photo of a finished filled pool"></div><h4>Final Step</h4><p>The final step is filling your pool and adding the proper chemicals.Your yard is left clean. Your pool is complete.</p></article>
  </div>
</section>

<section class="testimonial">
  <h2 class="section-title testimonial-title">Testimonial</h2>
  <div class="avatar" role="img" aria-label="Customer portrait"></div>
  <div class="person">Daniel Reyes<span class="role">FITNESS TRAINER</span></div>
  <svg class="quote-mark" width="34" height="22" viewBox="0 0 34 22"><path d="M4 0h8l-6 22H0zM20 0h8l-6 22h-6z" fill="#2f73c9"/></svg>
  <p class="quote">Cum soluta nobis est eligendi optio cumque nihil impedit quo minus id quod maxime placeat facere possimus, omnis voluptas assumenda est, omnis dolor repellendus.</p>
  <div class="pager"><span class="on"></span><span></span><span></span></div>
</section>

<section class="subscribe">
  <p>By subscribing to our mailing list you will&nbsp; get the latest news from us</p>
  <div class="field">Email address...
    <svg width="12" height="10" viewBox="0 0 12 10"><path d="m1 5 3.5 3.5L11 1" fill="none" stroke="#dfe7f0" stroke-width="1.6"/></svg>
  </div>
  <div class="submit">Submit</div>
</section>

<footer class="footer">
  <div class="col about">
    <h5>About Us</h5>
    <div class="footer-brand"><span class="dot"></span>Saguaro Pools</div>
    <p>Saguaro Pools was founded for one simple reason, to make a better pools. We are family owned and operated...</p>
    <a class="more">Read More...</a>
  </div>
  <div class="col blog">
    <h5>Latest Blog</h5>
    <div class="post" style="top:62px">
      <div class="thumb ph-pool" role="img" aria-label="Blog post photo of a pool"></div>
      <div><div class="meta">Earum Rerum &nbsp; Nam liberi<br>2 days ago</div><div class="title">Temporibus autem quibus dam et aut officiis...</div><a class="more">Read More...</a></div>
    </div>
    <div class="post" style="top:150px">
      <div class="thumb ph-night" role="img" aria-label="Blog post photo of a pool at dusk"></div>
      <div><div class="meta">Aliquam Qua &nbsp; Nihil Mole<br>3 days ago</div><div class="title">Sed ut perspiciatis undeom nis iste natus...</div><a class="more">Read More...</a></div>
    </div>
  </div>
  <div class="col contact">
    <h5>Contact Us</h5>
    <ul>
      <li><svg width="9" height="12" viewBox="0 0 9 12"><path d="M4.5 0A4.5 4.5 0 0 0 0 4.5C0 8 4.5 12 4.5 12S9 8 9 4.5A4.5 4.5 0 0 0 4.5 0zm0 6.3a1.8 1.8 0 1 1 0-3.6 1.8 1.8 0 0 1 0 3.6z" fill="#fff"/></svg><span>4820 W Mesquite Trail,<br>Phoenix, AZ 85000</span></li>
      <li><svg width="11" height="11" viewBox="0 0 11 11"><path d="M2.2 0 4 2.6 2.8 4a7 7 0 0 0 4.2 4.2L8.4 7 11 8.8 9.6 11C4 10.5.5 7 0 1.4z" fill="#fff"/></svg><span>Call Now! 555-214-0370</span></li>
      <li><svg width="12" height="11" viewBox="0 0 12 11"><rect x="0" y="2" width="12" height="9" rx="1" fill="#fff"/><rect x="3" y="0" width="6" height="3" fill="#fff"/></svg><span>Toll Free 1-800-555-0142</span></li>
      <li><svg width="12" height="11" viewBox="0 0 12 11"><rect x="0" y="3" width="12" height="8" rx="1" fill="#fff"/><rect x="2" y="0" width="8" height="4" fill="#fff" stroke="#20508f"/></svg><span>Fax 555-214-0371</span></li>
    </ul>
    <div class="social"><span></span><span></span><span></span><span></span></div>
    <div class="social-line"></div>
  </div>
</footer>

<div class="bottom">
  <span class="copy">© Copyright information here</span>
  <svg class="top-btn" width="28" height="28" viewBox="0 0 28 28"><circle cx="14" cy="14" r="12.5" fill="none" stroke="#0f2a4d" stroke-width="1.5"/><path d="M14 21V8M9 13l5-5 5 5" fill="none" stroke="#0f2a4d" stroke-width="1.5"/></svg>
</div>

</body>
</html>
```